Stationery Design Project

Hi All,

We need you to design stationary for a new Business and Accounting Advisory Firm. We have already got the logo designed and it is attached. If you could also if possible, match the fonts in your design to that on the logo’s provided.

What we need:
- Business Card
- A4 Letter head
- A4 Folders
- PPT template (Title page and regular page)

And what ever else you want to throw in.

We are in the process of getting the web site designed, however below is a list of websites which we like which will give you an understanding of the style that we are going for.

- plavoni.com
- brightfunnelo.com
- hourquillet.com
- artmarrowly.com

I look forward to your seeing your design.

Hi All,

I have just realised that I forgot that i need to include a Licensed Tallymasters image on the letter head, please find attaced as File 1. Could you please have this image in the bottom left header.

Regards,

Gareth

Industry/Entity Type

Business

Requirements
Must have
• Outputs:
- Documents ready to print
- Generic editable information
- Pdf copies of the documents
- Word version of letterhead

```html
<!DOCTYPE html>
<html lang="en">
<head>
<meta charset="utf-8">
<title>Tindale Partners — Business Cards</title>
<link href="https://fonts.googleapis.com/css2?family=EB+Garamond:wght@500&family=Arimo:wght@400&display=swap" rel="stylesheet">
<style>
  :root {
    --backdrop: #e4e4e4;
    --card: #f4f5f7;
    --navy: #3a5a9c;
    --sky: #3fbcd8;
    --deep-blue: #3a569e;
    --orange: #f58220;
    --amber: #fdc43a;
    --text-grey: #767676;
  }
  html, body {
    margin: 0;
    padding: 0;
    width: 1200px;
    height: 1000px;
    overflow: hidden;
    background: var(--backdrop);
  }
  .canvas {
    position: relative;
    width: 1200px;
    height: 1000px;
  }
  .card {
    position: absolute;
  }
  .card svg.card-shape {
    position: absolute;
    left: 0;
    top: 0;
  }
  .card-front {
    left: 313px;
    top: 165px;
    width: 594px;
    height: 297px;
  }
  .card-back {
    left: 313px;
    top: 525px;
    width: 592px;
    height: 297px;
  }
  .brand {
    position: absolute;
    left: 94px;
    top: 120px;
    display: flex;
    align-items: center;
  }
  .brand-dot {
    width: 52px;
    height: 52px;
    border-radius: 50%;
    background: var(--orange);
    margin-right: 22px;
  }
  .brand-name {
    font-family: "EB Garamond", Georgia, serif;
    font-weight: 500;
    font-size: 39px;
    line-height: 1;
    color: var(--navy);
    margin: 0;
  }
  .brand-tagline {
    font-family: "Arimo", Arial, sans-serif;
    font-size: 14px;
    letter-spacing: 6.8px;
    color: var(--navy);
    margin: 7px 0 0 0;
  }
  .back-text {
    font-family: "Arimo", Arial, sans-serif;
    font-size: 17px;
    color: var(--text-grey);
    position: absolute;
    margin: 0;
  }
  .website {
    left: 47px;
    top: 99px;
    font-size: 18px;
    letter-spacing: 0.9px;
  }
  .contact-list {
    left: 313px;
    top: 99px;
    list-style: none;
    padding: 0;
  }
  .contact-list li {
    display: flex;
    height: 25.5px;
  }
  .contact-label {
    width: 31px;
    color: var(--orange);
  }
  .address {
    left: 344px;
    top: 219px;
    line-height: 23px;
  }
</style>
</head>
<body>
<div class="canvas">

  <section class="card card-front" aria-label="Business card front">
    <svg class="card-shape" width="594" height="297" viewBox="0 0 594 297">
      <path d="M0 0 H494 A100 100 0 0 1 594 100 V297 H0 Z" fill="var(--card)"/>
    </svg>
    <div class="brand">
      <div class="brand-dot"></div>
      <div>
        <p class="brand-name">Tindale Partners</p>
        <p class="brand-tagline">Business Advisors</p>
      </div>
    </div>
  </section>

  <section class="card card-back" aria-label="Business card back">
    <svg class="card-shape" width="592" height="297" viewBox="0 0 592 297">
      <defs>
        <linearGradient id="blue-band" x1="0" y1="0" x2="0" y2="1">
          <stop offset="0" stop-color="#3fbcd8"/>
          <stop offset="1" stop-color="#3a569e"/>
        </linearGradient>
        <linearGradient id="orange-band" x1="0" y1="0" x2="0" y2="1">
          <stop offset="0" stop-color="#f58220"/>
          <stop offset="1" stop-color="#fdc43a"/>
        </linearGradient>
      </defs>
      <path d="M100 0 H592 V297 H0 V100 A100 100 0 0 1 100 0 Z" fill="var(--card)"/>
      <rect x="287" y="0" width="305" height="70" fill="url(#blue-band)" role="img" aria-label="Blue decorative corner wave"/>
      <rect x="0" y="220" width="332" height="77" fill="url(#orange-band)" role="img" aria-label="Orange decorative corner wave"/>
    </svg>
    <p class="back-text website">www.xxxxxxxx.com.au</p>
    <ul class="back-text contact-list">
      <li><span class="contact-label">T</span><span>03 000 000</span></li>
      <li><span class="contact-label">F</span><span>03 000 000</span></li>
      <li><span class="contact-label">M</span><span>0400 000 000</span></li>
      <li><span class="contact-label">E</span><span>xxxxx@xxxxxx.com.au</span></li>
    </ul>
    <p class="back-text address">000 Lorem Street, Aenean<br>Anriean VIC 3000</p>
  </section>

</div>
</body>
</html>
```